ebook cover: book 4 in the You Grow Pepper series. Warmth Beyond Fences

I am wanting a striking cover to bring the forth book in a spiritual journey series to an audience ready to meet new characters and get excited again! White backgrounds, red titles (any font), subtitles to introduce a new major character in the series of ten (same fonts please as the original, You Grow Pepper), and one emblematic, slightly mysterious image. Please keep to the same colour tones as the original, but the lead image need not be gray. Let's please try to use the "light flash" that is on the tin can in You Grow Pepper somehow, in your own way. It is meant to signify the other side, or the higher light, or some such inference.

Book details:
Title: Warmth Beyond Fences
Subtitle: Elder Corvanel brings the message
Image: silver hourglass
Author: Mabel Quinlow, Ph.D
Strap quote: "Quinlow is smart, savvy and full of ideas," Harwick Evening Ledger

Please do your best: this one is going in competition of spiritual healers!

Thanks! :)

```html
<!DOCTYPE html>
<html lang="en">
<head>
<meta charset="utf-8">
<title>Warmth Beyond Fences — Ebook Cover</title>
<link rel="stylesheet" href="https://fonts.googleapis.com/css2?family=Bebas+Neue&family=Open+Sans:wght@400;600&display=swap">
<style>
  :root {
    --paper: #ffffff;
    --title-red: #c0161b;
    --ink: #1f1a1a;
    --author-grey: #6b6565;
    --silver-light: #e6dfdc;
    --silver-mid: #cbc1be;
    --glow: #f5d6c2;
  }
  html, body {
    margin: 0;
    padding: 0;
    overflow: hidden;
    background: var(--paper);
  }
  .cover {
    position: relative;
    width: 811px;
    height: 1200px;
    background: var(--paper);
    overflow: hidden;
    font-family: "Open Sans", sans-serif;
  }
  .strap-quote {
    position: absolute;
    top: 36px;
    left: 0;
    width: 100%;
    text-align: center;
    margin: 0;
    font-size: 18px;
    letter-spacing: 0.2px;
    color: var(--ink);
  }
  .title {
    position: absolute;
    top: 146px;
    left: 0;
    width: 100%;
    text-align: center;
    margin: 0;
    font-family: "Bebas Neue", sans-serif;
    font-weight: 400;
    font-size: 98px;
    line-height: 1;
    letter-spacing: -0.5px;
    color: var(--title-red);
  }
  .subtitle {
    position: absolute;
    top: 238px;
    left: 0;
    width: 100%;
    text-align: center;
    margin: 0;
    font-weight: 600;
    font-size: 40px;
    line-height: 44px;
    letter-spacing: 9px;
    color: var(--ink);
    text-transform: uppercase;
  }
  .lead-image {
    position: absolute;
    top: 380px;
    left: 190px;
    width: 430px;
    height: 625px;
    background: radial-gradient(ellipse 50% 50% at 50% 42%,
      var(--glow) 0%,
      var(--silver-light) 45%,
      var(--silver-mid) 75%,
      var(--paper) 100%);
  }
  .author {
    position: absolute;
    top: 1074px;
    left: 0;
    width: 100%;
    text-align: center;
    margin: 0;
    font-weight: 400;
    font-size: 48px;
    letter-spacing: 4px;
    color: var(--author-grey);
  }
  .author .degree {
    font-variant: small-caps;
    letter-spacing: 2px;
  }
</style>
</head>
<body>
  <div class="cover">
    <p class="strap-quote">"QUINLOW IS SMART, SAVVY AND FULL OF IDEAS," HARWICK EVENING LEDGER</p>
    <h1 class="title">WARMTH BEYOND FENCES</h1>
    <h2 class="subtitle">Elder Corvanel<br>brings the message</h2>
    <div class="lead-image" role="img" aria-label="Photograph of a silver hourglass with white sand, lit from behind by a soft warm light flash"></div>
    <p class="author">MABEL QUINLOW <span class="degree">Ph.D.</span></p>
  </div>
</body>
</html>
```